Tallow & Mersey Needs New Stationery / Letterhead Design

We need new stationery to match our new logo (attached). Tallow & Mersey is a 34 year old nationwide law firm located in Houston Tx. They do personal injury law and pharmaceutical litigation.

WE DO NOT NEED BUSINESS CARDS.

Attached are several different file formats of the new logo.

Reason: We will make a decision in the next couple days. Finalizing edits now. Thank you!

Target Market(s)

consumers who have been injured due to the negligence of another or by a pharmaceutical drug or defective medical device. Also co-counsel and opposing counsel (law firms0.

Industry/Entity Type

Law Firm

Requirements
Must have
• logo
• Tallow & Mersey, LLP
• 7183 Corvid Lane, Suite 1000
• Brenford, TX 75591
• Tel: (555) 408-1936
• Fax: (555) 408-2275
• www.tallowandmersey.example
• Must have colors in the logo.
• Make the font go with the logo - not necessarily the same, but something that goes well with it.

```html
<!DOCTYPE html>
<html lang="en">
<head>
<meta charset="utf-8">
<title>Tallow &amp; Mersey Stationery</title>
<link rel="stylesheet" href="https://fonts.googleapis.com/css2?family=Cinzel:wght@500&family=Jost:wght@400;600&display=swap">
<style>
  :root {
    --navy: #2b3e63;
    --rule-grey: #a9a9a9;
    --paper: #f4f4f4;
    --backdrop: #d3d3d3;
    --ink: #3c3c3c;
  }
  * { box-sizing: border-box; margin: 0; padding: 0; }
  html, body { width: 1200px; height: 760px; overflow: hidden; background: var(--backdrop); }
  .canvas { position: relative; width: 1200px; height: 760px; }
  .sheet { position: absolute; background: var(--paper); overflow: hidden; }

  .letterhead { left: 67px; top: 66px; width: 486px; height: 628px; }
  .envelope-front { left: 588px; top: 66px; width: 542px; height: 236px; }
  .envelope-back { left: 588px; top: 338px; width: 542px; height: 236px; }

  .firm-name {
    font-family: "Cinzel", serif; font-weight: 500; color: var(--navy);
    display: flex; align-items: center; gap: 7px; white-space: nowrap;
  }
  .firm-name .mark { width: 14px; height: 14px; background: var(--navy); flex: none; }

  .letterhead .firm-name { position: absolute; left: 35px; top: 40px; font-size: 18px; }
  .contact {
    position: absolute; left: 363px; top: 34px;
    font-family: "Jost", sans-serif; font-size: 6.5px; line-height: 8.4px; color: var(--ink);
  }
  .contact .address { border-left: 1.5px solid var(--navy); padding-left: 8px; }
  .contact .address strong { color: var(--navy); font-weight: 600; }
  .contact .phones { border-left: 1px solid var(--rule-grey); padding-left: 8px; margin-top: 6px; }
  .contact .phones div { display: flex; align-items: center; gap: 4px; }
  .contact svg { width: 6px; height: 6px; fill: var(--navy); }

  .footer-band { position: absolute; left: 0; right: 0; bottom: 0; }
  .footer-band .rule-row { display: flex; align-items: center; gap: 7px; }
  .footer-band .rule { height: 2px; background: var(--rule-grey); }
  .footer-band .bar { height: 9px; background: var(--navy); margin-top: 5px; }
  .web {
    font-family: "Jost", sans-serif; font-size: 6.5px; letter-spacing: .3px; color: var(--ink);
    text-transform: uppercase; white-space: nowrap;
  }
  .web b { color: var(--navy); font-weight: 600; }
  .letterhead .rule.lead { width: 343px; }
  .letterhead .rule.tail { flex: 1; }
  .envelope-front .rule.lead { width: 402px; }
  .envelope-front .rule.tail { flex: 1; }

  .envelope-front .firm-name { position: absolute; left: 22px; top: 34px; font-size: 17px; }
  .return-address {
    position: absolute; left: 22px; width: 124px; top: 91px; text-align: center;
    font-family: "Jost", sans-serif; font-size: 5.8px; line-height: 7px; color: var(--ink);
  }

  .flap { position: absolute; left: 0; top: 0; width: 542px; height: 80px; }
  .flap-name {
    position: absolute; left: 0; right: 0; top: 30px; justify-content: center;
    font-size: 13px; color: var(--paper);
  }
  .back-web {
    position: absolute; left: 0; right: 0; top: 206px; text-align: center;
    font-family: "Jost", sans-serif; font-size: 6.5px; color: var(--ink);
  }
  .back-web b { color: var(--navy); font-weight: 600; }
</style>
</head>
<body>
<main class="canvas">

  <section class="sheet letterhead">
    <div class="firm-name"><span class="mark"></span>Tallow &amp; Mersey</div>
    <div class="contact">
      <div class="address">
        <strong>Tallow &amp; Mersey, LLP</strong><br>
        7183 Corvid Lane, Suite 1000<br>
        Brenford, TX 75591
      </div>
      <div class="phones">
        <div><svg viewBox="0 0 10 10" aria-hidden="true"><path d="M2 0.5 L3.8 2.6 L2.9 3.8 Q4 6 6.2 7.1 L7.4 6.2 L9.5 8 L8.3 9.5 Q3.5 9 0.5 1.7 Z"/></svg>(555) 408-1936</div>
        <div><svg viewBox="0 0 10 10" aria-hidden="true"><rect x="2.5" y="0.5" width="5" height="3"/><rect x="0.5" y="4" width="9" height="5.5" rx="1"/></svg>(555) 408-2275</div>
      </div>
    </div>
    <div class="footer-band">
      <div class="rule-row">
        <span class="rule lead"></span>
        <span class="web">www.<b>tallowandmersey</b>.example</span>
        <span class="rule tail"></span>
      </div>
      <div class="bar"></div>
    </div>
  </section>

  <section class="sheet envelope-front">
    <div class="firm-name"><span class="mark"></span>Tallow &amp; Mersey</div>
    <div class="return-address">7183 Corvid Lane, Suite 1000<br>Brenford, TX 75591</div>
    <div class="footer-band">
      <div class="rule-row">
        <span class="rule lead"></span>
        <span class="web">www.<b>tallowandmersey</b>.example</span>
        <span class="rule tail"></span>
      </div>
      <div class="bar"></div>
    </div>
  </section>

  <section class="sheet envelope-back">
    <svg class="flap" viewBox="0 0 542 80" aria-hidden="true">
      <path d="M2 0 H540 L522 72 Q520 78 512 78 H32 Q24 78 22 72 Z" fill="var(--navy)"/>
    </svg>
    <div class="firm-name flap-name">Tallow &amp; Mersey</div>
    <div class="back-web">www.<b>tallowandmersey</b>.example</div>
  </section>

</main>
</body>
</html>
```